Want to go online this week, rush project, everything is there, just make it pretty

I need a pretty html5/css template for a already made site. Please do not rearrange anything unless you feel you can simplify the design. I have a raw site. Please play with the site by making an account with coupon code PLUMWALKERS for free signup. Log in, log out, download as many designs as you can, then log in and log out. See everything cause it's brand new and I need it neat and pretty over the next few days if not sooner. So, after all that, the site is http://StitchloomPatternHub.example
Updates

Is anyone working on something to submit? If you have something please submit asap as I will be closing this Sat night or Sunday morning

Industry/Entity Type

Online

Coding

Coded - Design and coding required

```html
<!DOCTYPE html>
<html lang="en">
<head>
<meta charset="utf-8">
<title>Stitchloom Pattern Hub</title>
<link href="https://fonts.googleapis.com/css2?family=Open+Sans:wght@400;600;700&family=Courier+Prime&display=swap" rel="stylesheet">
<style>
:root{
  --pink:#e07bb3;
  --pink-dot:#f0a9c8;
  --pink-soft:#f7dbe9;
  --yellow:#f2c811;
  --green:#8ec95a;
  --title-green:#6fb34a;
  --text:#333;
  --muted:#9a9a9a;
  --line:#e3e3e3;
  --panel:#f2f2f2;
  --paper:#e9e9e9;
  --footer:#2c2c2c;
  --footer-text:#bdbdbd;
}
*{margin:0;padding:0;box-sizing:border-box}
html,body{width:898px;height:1200px;overflow:hidden;background:#fff}
body{position:relative;font-family:"Open Sans",sans-serif;color:var(--text)}
.abs{position:absolute}
.brand{left:76px;top:40px;display:flex;align-items:center;gap:12px;height:80px}
.brand-mark{flex:none;width:64px;height:64px;border-radius:50%;background:var(--pink-soft)}
.brand-name{font-size:17px;font-weight:600;color:var(--pink);white-space:nowrap;letter-spacing:.1px}
.icon{width:26px;height:26px;border-radius:50%;top:21px}
.icon svg{display:block}
.cart-total{left:790px;top:27px;font-size:12px;color:#777}
.rule{height:1px;background:var(--line)}
.notify{right:146px;top:75px;font-size:10px;color:var(--muted)}
.like{left:758px;top:72px;display:flex;height:16px;font-size:9px}
.like b{background:#4a67a8;color:#fff;padding:1px 6px;border-radius:2px;font-weight:700}
.like span{border:1px solid #aaa;margin-left:3px;padding:0 3px;color:#555;background:#fff}
.nav{top:120px;font-size:12px;color:#999;letter-spacing:.2px}
.nav.active{color:var(--pink)}
.slider{left:75px;top:164px;width:749px;height:300px;border:2px dotted var(--pink-dot)}
.slide{left:83px;top:173px;width:731px;height:283px;background:radial-gradient(ellipse at 55% 45%,#c7321f 0%,#6a1a14 35%,#1b1818 70%)}
.arrow{top:303px;width:20px;height:20px;border-radius:50%;background:rgba(255,255,255,.55)}
.promo{top:478px;width:241px;height:100px;background:var(--paper);text-align:center;font-family:"Courier Prime",monospace;color:#222}
.promo h2{font-weight:400;font-size:24px;line-height:25px}
.promo p{font-size:9.5px;line-height:14px;margin-top:7px;color:#444}
.panel{left:74px;top:594px;width:750px;height:446px;background:var(--panel)}
.panel-title{left:74px;top:607px;width:750px;text-align:center;font-weight:700;font-size:14px;color:var(--title-green)}
.card{width:135px;height:164px;background:#fff;border:1px solid #ddd;text-align:center}
.card .thumb{margin:7px auto 0;width:120px;height:95px}
.card h3{font-size:10.5px;font-weight:600;margin-top:8px;color:#222}
.card p{font-size:9px;color:var(--muted);line-height:14px;margin-top:2px}
.dot{top:1009px;width:5px;height:5px;border-radius:50%;background:#ccc}
.dot.on{background:#777}
.footer{left:0;top:1090px;width:898px;height:110px;background:var(--footer)}
.flink{top:1111px;font-size:10.5px;color:var(--footer-text)}
.copyright{left:76px;top:1163px;font-size:10.5px;color:var(--footer-text)}
.social{top:1158px;width:24px;height:24px;border-radius:50%}
</style>
</head>
<body>
<div class="abs brand">
  <div class="brand-mark"></div>
  <div class="brand-name">StitchloomPatternHub.example</div>
</div>

<div class="abs icon" style="left:695px;background:#e98db8">
  <svg width="26" height="26"><circle cx="12" cy="12" r="4.5" fill="none" stroke="#fff" stroke-width="2"/><line x1="15" y1="15" x2="19" y2="19" stroke="#fff" stroke-width="2"/></svg>
</div>
<div class="abs icon" style="left:727px;background:var(--yellow)">
  <svg width="26" height="26"><polygon points="13,6 15,11 20,11 16,14 17.5,19 13,16 8.5,19 10,14 6,11 11,11" fill="#fff"/></svg>
</div>
<div class="abs icon" style="left:757px;background:var(--green)">
  <svg width="26" height="26"><path d="M7 11h12l-1.5 7h-9z" fill="#fff"/><path d="M10 11l3-4 3 4" fill="none" stroke="#fff" stroke-width="1.5"/></svg>
</div>
<div class="abs cart-total">$00.00</div>

<div class="abs rule" style="left:496px;top:62px;width:328px"></div>
<div class="abs notify">Get notified of new designs!</div>
<div class="abs like"><b>Like</b><span>1.1k</span></div>
<div class="abs rule" style="left:496px;top:102px;width:328px"></div>

<div class="abs nav active" style="left:537px">HOME</div>
<div class="abs nav" style="left:602px">REGISTER</div>
<div class="abs nav" style="left:684px">ACCOUNT</div>
<div class="abs nav" style="left:770px">CONTACT</div>

<div class="abs slider"></div>
<div class="abs slide" role="img" aria-label="Close-up of a sewing machine foot stitching red swirl embroidery on black fabric"></div>
<div class="abs arrow" style="left:99px"></div>
<div class="abs arrow" style="left:779px"></div>

<div class="abs promo" style="left:76px;padding-top:18px"><h2>Register</h2><p>for unlimited embroidery design<br>downloads!</p></div>
<div class="abs promo" style="left:330px;padding-top:18px"><h2>Get All</h2><p>Designs on DVD</p></div>
<div class="abs promo" style="left:582px;padding-top:10px"><h2>Today’s<br>Free Design</h2><p>Click here</p></div>

<div class="abs rule" style="left:74px;top:592px;width:750px;background:#d8d8d8"></div>
<div class="abs panel"></div>
<div class="abs panel-title">OUR DESIGNS</div>

<div class="abs card" style="left:82px;top:641px"><div class="thumb" role="img" aria-label="Embroidered witch girl with cauldron" style="background:linear-gradient(#f4f4f6,#d9d2e4)"></div><h3>Witch Marigold</h3><p>10 Designs<br>All Fit the 4x4 Hoop</p></div>
<div class="abs card" style="left:232px;top:641px"><div class="thumb" role="img" aria-label="Green appliqué monster" style="background:radial-gradient(circle,#7fd04a,#e8eaea 70%)"></div><h3>Witch Marigold</h3><p>10 Designs<br>All Fit the 4x4 Hoop</p></div>
<div class="abs card" style="left:382px;top:641px"><div class="thumb" role="img" aria-label="Swirl-line cat face embroidery" style="background:linear-gradient(#eef2f3,#e3d6cf)"></div><h3>Witch Marigold</h3><p>10 Designs<br>All Fit the 4x4 Hoop</p></div>
<div class="abs card" style="left:532px;top:641px"><div class="thumb" role="img" aria-label="Embroidered girl holding a pumpkin" style="background:linear-gradient(#e4e2e6,#cbc6cc)"></div><h3>Witch Marigold</h3><p>10 Designs<br>All Fit the 4x4 Hoop</p></div>
<div class="abs card" style="left:682px;top:641px"><div class="thumb" role="img" aria-label="Halloween treat bags with candy" style="background:linear-gradient(#6a5a3a,#e07a25)"></div><h3>Witch Marigold</h3><p>10 Designs<br>All Fit the 4x4 Hoop</p></div>

<div class="abs card" style="left:82px;top:822px"><div class="thumb" role="img" aria-label="Black line tiger head embroidery" style="background:linear-gradient(#f2f2f2,#cfcfcf)"></div><h3>Witch Marigold</h3><p>10 Designs<br>All Fit the 4x4 Hoop</p></div>
<div class="abs card" style="left:232px;top:822px"><div class="thumb" role="img" aria-label="Embroidered lady in purple dress walking a teddy bear" style="background:linear-gradient(#e6e0ec,#c9b9d8)"></div><h3>Witch Marigold</h3><p>10 Designs<br>All Fit the 4x4 Hoop</p></div>
<div class="abs card" style="left:382px;top:822px"><div class="thumb" role="img" aria-label="Purple script monogram letter with chevron border" style="background:linear-gradient(#3fb7c4 0,#efe4cf 15%,#efe4cf 85%,#3fb7c4 100%)"></div><h3>Witch Marigold</h3><p>10 Designs<br>All Fit the 4x4 Hoop</p></div>
<div class="abs card" style="left:532px;top:822px"><div class="thumb" role="img" aria-label="Blue embroidered dragon" style="background:linear-gradient(#e6eaee,#8bb5cf)"></div><h3>Witch Marigold</h3><p>10 Designs<br>All Fit the 4x4 Hoop</p></div>
<div class="abs card" style="left:682px;top:822px"><div class="thumb" role="img" aria-label="Owl in a witch hat on a broomstick" style="background:linear-gradient(#eeeef2,#6c5aa3)"></div><h3>Witch Marigold</h3><p>10 Designs<br>All Fit the 4x4 Hoop</p></div>

<div class="abs dot on" style="left:416px"></div>
<div class="abs dot" style="left:431px"></div>
<div class="abs dot" style="left:447px"></div>
<div class="abs dot" style="left:463px"></div>
<div class="abs dot" style="left:478px"></div>

<div class="abs rule" style="left:74px;top:1043px;width:750px;background:#d8d8d8"></div>

<div class="abs footer"></div>
<div class="abs flink" style="left:147px">• Home</div>
<div class="abs flink" style="left:231px">• About us</div>
<div class="abs flink" style="left:351px">• Register</div>
<div class="abs flink" style="left:467px">• Account</div>
<div class="abs flink" style="left:583px">• Search</div>
<div class="abs flink" style="left:692px">• Contact us</div>
<div class="abs rule" style="left:74px;top:1142px;width:750px;background:#444"></div>
<div class="abs copyright">Copyright © 2014 Stitchloom Pattern Hub.&nbsp;&nbsp;All rights reserved.</div>
<div class="abs social" style="left:766px;background:#3b5a9a"></div>
<div class="abs social" style="left:799px;background:#2aa3e0"></div>
</body>
</html>
```